高品質・高級感・親しみやすさ・かっこよさ・スタンダードではない
のイメージでお願いいたします。

記載項目の裏表の配置はお任せいたします。

ロゴ・店舗写真を添付致します。(ロゴの画像部分と文字部分を切り離して使って頂いても構いません。)
記載項目
ジムロゴ・役職名・名前・住所・電話番号・Fax・HPアドレス・メールアドレス・智頭

提案の中で、ある程度選考を進めた後何名かに実際の住所等の情報を提供いたします。
掲載事項、智頭ではなく、地図です。訂正させて頂きます。
ロゴの制作者様から頂きました、看板やパンフレットイメージを追加で添付させて頂きます。
提案が集まらないので、期間を延長致します。
再度延長させて頂きます。現在提案して頂いてるかたに、修正をお願いするかもしれません。よろしくお願いいたします。
追記致します。

1、添付している、photo4の写真にある木目壁面の看板の画像を参考にしていただいて、背景に木目を利用したもの。
2、ロゴをデボス調に加工したもの

上記の希望に沿った提案をお願いいたします。是非よろしくお願いいたします。
19日の追記を訂正いたします。私の書き方が悪く、うまく伝わっていませんでした。大変申し訳ございません。

パターン1、添付している、photo4の写真にある木目壁面に金箱文字の画像を参考にしていただき、薄い木目調の背景に、箱文字のロゴを使ったもの
パターン2、白基調の背景に、デボス加工を施したロゴを使ったもの(参考としてphoto5を添付いたします。)

どちらかのパターンでのご提案をお願いいたします。
先日追記しました、パターン2の
白基調の背景に、デボス加工を施したロゴを使ったもの
を提案いただいている方へ、追記いたします。

私が参考としてあげたデボスの画像が色が無かったので申し訳ございませんでした。
デボス加工をした上で、色は残していただきたいと思います。

何度も追記しまして大変申し訳ございませんが、よろしくお願いいたします。

社内での協議の結果、決定致しました。

多くのご提案ありがとうございました。
また、追記を何度も重ねてしまいご迷惑をおかけいたしました。

```html
<!DOCTYPE html>
<html lang="ja">
<head>
<meta charset="utf-8">
<title>Core Body Studio – 名刺</title>
<link rel="stylesheet" href="https://fonts.googleapis.com/css2?family=Cormorant+Garamond:wght@400&family=Noto+Serif+JP:wght@400;500&display=swap">
<style>
  :root {
    --paper: #f7f7f5;
    --paper-shade: #ecebe8;
    --ink: #2b2b2b;
    --logo-grey: #a9a9a9;
    --edge: #d8d8d8;
  }
  html, body {
    margin: 0;
    padding: 0;
    width: 769px;
    height: 1200px;
    overflow: hidden;
    background: var(--paper);
  }
  .card {
    position: relative;
    width: 769px;
    height: 1200px;
    box-sizing: border-box;
    border: 1px solid var(--edge);
    background: radial-gradient(ellipse at 50% 35%, #fbfbfa 0%, var(--paper) 55%, var(--paper-shade) 100%);
    font-family: "Noto Serif JP", serif;
    color: var(--ink);
  }
  .brand {
    position: absolute;
    top: 250px;
    left: 0;
    width: 100%;
    text-align: center;
  }
  .brand-mark {
    display: block;
    margin: 0 auto 44px;
  }
  .brand-name {
    font-family: "Cormorant Garamond", serif;
    font-weight: 400;
    font-size: 62px;
    letter-spacing: 3px;
    color: var(--logo-grey);
    margin: 0;
  }
  .person {
    position: absolute;
    top: 622px;
    left: 292px;
  }
  .person-title {
    font-size: 22px;
    letter-spacing: 2px;
    margin: 0 0 14px;
  }
  .person-name {
    font-size: 38px;
    font-weight: 500;
    letter-spacing: 6px;
    margin: 0 0 6px;
    line-height: 1.2;
  }
  .person-roman {
    font-size: 21px;
    letter-spacing: 1px;
    margin: 0;
  }
  .contact {
    position: absolute;
    top: 972px;
    left: 226px;
    font-size: 22px;
    line-height: 1.45;
    margin: 0;
  }
  .contact span + span { margin-left: 32px; }
</style>
</head>
<body>
  <div class="card">
    <header class="brand">
      <svg class="brand-mark" width="120" height="120" viewBox="0 0 120 120" aria-hidden="true">
        <circle cx="60" cy="60" r="54" fill="none" stroke="var(--logo-grey)" stroke-width="2"/>
      </svg>
      <h1 class="brand-name">Core Body Studio</h1>
    </header>

    <section class="person">
      <p class="person-title">チーフトレーナー</p>
      <p class="person-name">佐藤健一</p>
      <p class="person-roman">SATO KENICHI</p>
    </section>

    <address class="contact" style="font-style:normal">
      〒150-0041 東京都渋谷区神南4-5-6△△ビル<br>
      <span>TEL : 03-2222-3333</span><span>FAX : 03-2222-3334</span><br>
      MAIL : info@corebodystudio.jp
    </address>
  </div>
</body>
</html>
```